Signage Design Project - Florida Vacation Resort Monument Sign

I need a design for the main identification sign outside of a resort in Florida. This is a sign that will be located at ground level near the entrance to the resort.

Text to include:

"4818" (This is the property address numbers, no street name necessary)

"Coral Haven" (This is the name of the resort)

"Heated Pool" (bullet point)
"Tiki Hut" (bullet point)
"Beach Access" (bullet point)

"Weekly/Monthly Rentals" (text to appear at bottom of sign)

Dimensions: 55.5"wide x 43.5"tall

Some design elements can protrude from the dimensions, as long as they are not too thin. It will ultimately need to be cut out of wood and if a design element is thin and sticks out of the box, it will be likely to break off.

***The artwork must be vectored.***

Please use whatever design elements you'd like in full color. A palm tree might make sense because of the name "Coral Haven", but I don't want to limit your creativity!

The website is here: http://www.coral-haven-example.com

They have a tour your can click on at the bottom for more pictures to get a feel for the property.

```html
<!DOCTYPE html>
<html lang="en">
<head>
<meta charset="utf-8">
<title>Coral Haven – Monument Sign</title>
<link href="https://fonts.googleapis.com/css2?family=Overlock:wght@900&family=Kaushan+Script&family=Bebas+Neue&display=swap" rel="stylesheet">
<style>
  :root {
    --page-bg: #e7e4df;
    --sky-top: #cfe6f3;
    --sky-mid: #f4f9fc;
    --title-light: #9fd14a;
    --title-dark: #1f7a32;
    --rule-green: #2f8f3a;
    --bullet-fill: #fff31a;
    --ink: #111111;
    --star-fill: #fff7a6;
    --sea-deep: #1f4fa3;
    --sea-light: #35b4e6;
    --sand: #f6e6a3;
    --sand-light: #fbf3cf;
    --rental-band: #fdfbe8;
    --palm-green: #4fae3f;
    --palm-dark: #2b7a2f;
  }
  * { margin: 0; padding: 0; box-sizing: border-box; }
  html, body {
    width: 1200px;
    height: 836px;
    overflow: hidden;
    background: var(--page-bg);
  }
  .sign {
    position: absolute;
    left: 123px;
    top: 43px;
    width: 954px;
    height: 750px;
    box-shadow: 0 4px 14px rgba(0,0,0,0.25);
  }
  .sign svg { display: block; }
  .resort-name {
    font-family: "Overlock", "Trebuchet MS", sans-serif;
    font-weight: 900;
    font-size: 116px;
    letter-spacing: 6px;
  }
  .amenity {
    font-family: "Kaushan Script", cursive;
    font-size: 78px;
    fill: var(--bullet-fill);
    stroke: var(--ink);
    stroke-width: 2.5px;
    paint-order: stroke fill;
  }
  .star {
    fill: var(--star-fill);
    stroke: var(--ink);
    stroke-width: 2px;
  }
  .address {
    font-family: "Bebas Neue", "Arial Narrow", sans-serif;
    font-size: 46px;
    fill: var(--ink);
    letter-spacing: 3px;
  }
  .rentals {
    font-family: "Bebas Neue", "Arial Narrow", sans-serif;
    font-size: 106px;
    fill: var(--ink);
    letter-spacing: 1px;
  }
</style>
</head>
<body>
  <div class="sign">
    <svg width="954" height="750" viewBox="0 0 954 750" xmlns="http://www.w3.org/2000/svg">
      <defs>
        <linearGradient id="sky" x1="0" y1="0" x2="0" y2="1">
          <stop offset="0" stop-color="var(--sky-top)"/>
          <stop offset="0.55" stop-color="var(--sky-mid)"/>
          <stop offset="1" stop-color="var(--sky-top)"/>
        </linearGradient>
        <linearGradient id="title-green" x1="0" y1="0" x2="0" y2="1">
          <stop offset="0" stop-color="var(--title-light)"/>
          <stop offset="1" stop-color="var(--title-dark)"/>
        </linearGradient>
        <linearGradient id="sea" x1="0" y1="0" x2="1" y2="0">
          <stop offset="0" stop-color="var(--sea-deep)"/>
          <stop offset="0.5" stop-color="var(--sea-light)"/>
          <stop offset="1" stop-color="var(--sea-deep)"/>
        </linearGradient>
        <linearGradient id="sand" x1="0" y1="0" x2="0" y2="1">
          <stop offset="0" stop-color="var(--sand-light)"/>
          <stop offset="1" stop-color="var(--sand)"/>
        </linearGradient>
        <radialGradient id="palm" cx="0.5" cy="0.35" r="0.6">
          <stop offset="0" stop-color="var(--palm-green)"/>
          <stop offset="1" stop-color="var(--palm-dark)" stop-opacity="0.85"/>
        </radialGradient>
        <filter id="title-shadow" x="-5%" y="-10%" width="110%" height="130%">
          <feDropShadow dx="3" dy="4" stdDeviation="0" flood-color="#3a3a3a"/>
        </filter>
        <symbol id="star-shape" viewBox="-12 -12 24 24">
          <polygon class="star" points="0,-11 3,-3.6 11,-3.4 4.8,1.6 7,9.6 0,5 -7,9.6 -4.8,1.6 -11,-3.4 -3,-3.6"/>
        </symbol>
      </defs>

      <rect class="sky" x="0" y="0" width="954" height="750" fill="url(#sky)"/>

      <path class="title-rule" d="M8 60 Q477 -50 946 60" fill="none" stroke="var(--rule-green)" stroke-width="3"/>
      <path class="title-rule" d="M8 212 Q477 96 946 212" fill="none" stroke="var(--rule-green)" stroke-width="3"/>

      <text class="resort-name" x="477" y="144" text-anchor="middle" fill="url(#title-green)" filter="url(#title-shadow)">Coral Haven</text>

      <rect class="palm-area" x="16" y="340" width="234" height="308" rx="80" fill="url(#palm)" opacity="0.8"
            role="img" aria-label="Illustration of two leaning palm trees on the left shore"/>
      <rect class="palm-area" x="718" y="340" width="222" height="308" rx="80" fill="url(#palm)" opacity="0.8"
            role="img" aria-label="Illustration of two leaning palm trees on the right shore"/>

      <g class="amenities">
        <text class="amenity" x="474" y="248" text-anchor="middle" textLength="432" lengthAdjust="spacingAndGlyphs">Heated Pool</text>
        <text class="amenity" x="474" y="336" text-anchor="middle" textLength="446" lengthAdjust="spacingAndGlyphs">Beach Access</text>
        <text class="amenity" x="474" y="424" text-anchor="middle" textLength="302" lengthAdjust="spacingAndGlyphs">Tiki Hut</text>

        <use href="#star-shape" x="192" y="200" width="42" height="42"/>
        <use href="#star-shape" x="719" y="200" width="42" height="42"/>
        <use href="#star-shape" x="180" y="291" width="42" height="42"/>
        <use href="#star-shape" x="731" y="291" width="42" height="42"/>
        <use href="#star-shape" x="264" y="384" width="42" height="42"/>
        <use href="#star-shape" x="654" y="384" width="42" height="42"/>
      </g>

      <path class="sea" d="M0 536 Q477 500 954 536 L954 650 L0 650 Z" fill="url(#sea)"/>
      <path class="sand" d="M0 640 Q477 540 954 640 L954 650 L0 650 Z" fill="url(#sand)"/>

      <text class="address" x="477" y="634" text-anchor="middle">4818</text>

      <rect class="rental-band" x="0" y="647" width="954" height="103" fill="var(--rental-band)"/>
      <text class="rentals" x="477" y="735" text-anchor="middle" textLength="920" lengthAdjust="spacingAndGlyphs">WEEKLY/MONTHLY RENTALS</text>
    </svg>
  </div>
</body>
</html>
```